Tallwater Marketing Business Card

Business card using new logo for marketing consulting company based in Silicon Valley. Limited information on card now (name, phone number, email, website), but room to add mailing address later.

```html
<!DOCTYPE html>
<html lang="en">
<head>
<meta charset="utf-8">
<title>Tallwater Marketing Business Card</title>
<link rel="stylesheet" href="https://fonts.googleapis.com/css2?family=Open+Sans:wght@400;600&family=Ubuntu:wght@400;500&display=swap">
<style>
  :root {
    --backdrop: #2b2b2b;
    --brand-blue: #1fb4e4;
    --brand-blue-deep: #1a9fcc;
    --paper: #f4f4f4;
    --paper-shade: #e2e2e2;
    --ink: #222326;
    --ink-soft: #3a3b3e;
    --brand-name: #3aaee0;
    --rule-light: rgba(255,255,255,0.75);
  }
  * { box-sizing: border-box; margin: 0; padding: 0; }
  html, body {
    width: 1200px; height: 992px; overflow: hidden;
    background: var(--backdrop);
    font-family: "Ubuntu", "Open Sans", sans-serif;
  }
  .card {
    position: absolute; left: 250px; width: 700px; height: 400px;
    box-shadow: 0 14px 30px rgba(0,0,0,0.5);
    overflow: hidden;
  }
  /* Back of card */
  .card-back {
    top: 62px;
    background: linear-gradient(180deg, #ffffff 0%, var(--paper-shade) 100%);
  }
  .card-back .band {
    position: absolute; top: 0; bottom: 0; width: 92px;
    background: var(--brand-blue);
  }
  .card-back .band-left { left: 0; box-shadow: 6px 0 10px rgba(0,0,0,0.12); }
  .card-back .band-right { right: 0; box-shadow: -6px 0 10px rgba(0,0,0,0.12); }
  .brand-lockup {
    display: flex; flex-direction: column; align-items: center; gap: 14px;
  }
  .card-back .brand-lockup {
    position: absolute; left: 0; right: 0; top: 128px;
  }
  .brand-mark {
    width: 54px; height: 54px; border-radius: 50%;
    background: var(--brand-blue);
  }
  .brand-name {
    font-family: "Ubuntu", sans-serif; font-weight: 400;
    color: var(--brand-name); font-size: 30px; letter-spacing: 1px;
    text-transform: uppercase; text-align: center; line-height: 1.1;
  }
  /* Front of card */
  .card-front {
    top: 512px; background: var(--paper);
  }
  .contact-panel {
    position: absolute; left: 0; top: 0; bottom: 0; width: 360px;
    background: linear-gradient(180deg, var(--brand-blue) 0%, var(--brand-blue-deep) 100%);
    box-shadow: 6px 0 12px rgba(0,0,0,0.18);
    padding: 44px 40px 0 52px; color: #fff;
  }
  .contact-group {
    border-top: 1.5px solid var(--rule-light);
    padding: 12px 0 16px;
  }
  .contact-group svg { display: block; width: 22px; height: 18px; margin-bottom: 6px; }
  .contact-group p {
    font-family: "Ubuntu", sans-serif; font-size: 16px; line-height: 1.35; letter-spacing: 0.3px;
  }
  .identity {
    position: absolute; left: 360px; right: 0; top: 0; bottom: 0;
    background: linear-gradient(135deg, #ffffff 0%, var(--paper-shade) 100%);
  }
  .identity .brand-lockup { margin-top: 40px; gap: 12px; }
  .identity .brand-mark { width: 46px; height: 46px; }
  .identity .brand-name { font-size: 24px; }
  .person {
    position: absolute; left: 40px; top: 220px;
  }
  .person-name {
    font-family: "Open Sans", sans-serif; font-weight: 400;
    font-size: 30px; letter-spacing: -0.5px; color: var(--ink);
  }
  .person-title {
    font-family: "Open Sans", sans-serif; font-weight: 400;
    font-size: 17px; color: var(--ink-soft); margin-top: 2px;
  }
</style>
</head>
<body>
  <section class="card card-back" aria-label="Card back">
    <div class="band band-left"></div>
    <div class="band band-right"></div>
    <div class="brand-lockup">
      <span class="brand-mark"></span>
      <span class="brand-name">Tallwater Marketing</span>
    </div>
  </section>

  <section class="card card-front" aria-label="Card front">
    <div class="contact-panel">
      <div class="contact-group">
        <svg viewBox="0 0 22 18" aria-hidden="true"><path d="M11 1 L1 9 H4 V17 H9 V12 H13 V17 H18 V9 H21 Z" fill="#fff"/></svg>
        <p>318 Harbor Lane<br>San Jose, CA 95112</p>
      </div>
      <div class="contact-group">
        <svg viewBox="0 0 22 18" aria-hidden="true"><path d="M2 6 Q11 -1 20 6 L17 8 L15 6 H7 L5 8 Z M5 9 H17 L19 17 H3 Z" fill="#fff"/><circle cx="11" cy="13" r="2.2" fill="#1fb4e4"/></svg>
        <p>+1 408-555-0142<br>+1 408-555-0187</p>
      </div>
      <div class="contact-group">
        <svg viewBox="0 0 22 18" aria-hidden="true"><rect x="1.5" y="1.5" width="19" height="12" fill="none" stroke="#fff" stroke-width="2"/><rect x="7" y="15" width="8" height="2" fill="#fff"/></svg>
        <p>support@tallwatermarketing.com<br>tallwatermarketing.com</p>
      </div>
    </div>
    <div class="identity">
      <div class="brand-lockup">
        <span class="brand-mark"></span>
        <span class="brand-name">Tallwater Marketing</span>
      </div>
      <div class="person">
        <h1 class="person-name">MR. LOREM IPSUM</h1>
        <p class="person-title">Certified Marketing Specialist</p>
      </div>
    </div>
  </section>
</body>
</html>
```